Pictures required on web page

I would like change three existing pictures on my new website.

The site can be found here:
http://maplebarrelvaults.quillstudio.com.au/

The three pictures to be changed are on the home page:
Purchase- Mixed Packs
Wine Club - Let Us Choose
Education- Wine Courses

I would like somthing stylish, classic and understated that fits in with the theme and feel of the site. I know stylish is a subjective thing. At the moment, the current picture makes the text difficult to read on a destop. Plus I don't think they are a perfect fit for our website anyway. I've attached a photo of our wine course room and also me in the store. Please, don't feel as though you have to use these pictures, but they're there if you want them. However I'm open to completely different photos/graphics to be used.

```html
<!DOCTYPE html>
<html lang="en">
<head>
<meta charset="utf-8">
<title>Maplebarrel Winery Home</title>
<link rel="stylesheet" href="https://fonts.googleapis.com/css2?family=Roboto:wght@400;500&family=Roboto+Slab:wght@300;400;700&family=Montserrat:wght@400;500&display=swap">
<style>
:root{
  --chrome:#dfe5ec;
  --chrome-line:#b9c3cf;
  --header-top:#2c3d63;
  --header-bottom:#1f2c4b;
  --nav:#1a2336;
  --panel-navy:#253558;
  --panel-red:#b54a4a;
  --ink:#222;
  --white:#fff;
  --muted:#9fb0cc;
  --black:#000;
  --product-bg:#ecebe8;
}
*{box-sizing:border-box;margin:0;padding:0}
html,body{width:1200px;height:1200px;overflow:hidden;background:var(--white);font-family:"Roboto",sans-serif}
.canvas{position:relative;width:1200px;height:1200px;overflow:hidden}
.abs{position:absolute}

/* browser bar */
.tabstrip{left:0;top:0;width:1200px;height:38px;background:var(--chrome);border-bottom:1px solid var(--chrome-line)}
.tab{top:4px;height:34px;font-size:12.5px;color:var(--ink);display:flex;align-items:center;gap:6px;padding:0 10px;white-space:nowrap;overflow:hidden}
.tab .x{color:#888;margin-left:auto;font-size:14px}
.tab.active{background:var(--white);border:1px solid var(--chrome-line);border-bottom:none;border-radius:4px 4px 0 0}
.addressbar{left:0;top:38px;width:1200px;height:36px;background:#f3f5f8;border-bottom:1px solid var(--chrome-line)}
.url{left:-4px;top:4px;width:912px;height:26px;background:var(--white);border:1px solid #c5ccd6;font-size:12px;padding:5px 6px;color:#333}
.engine{left:918px;top:4px;width:282px;height:26px;background:var(--white);border:1px solid #c5ccd6;font-size:12px;color:#888;font-style:italic;padding:5px 8px 5px 38px}
.engine .sq{position:absolute;left:6px;top:5px;width:14px;height:14px;background:#4a78c8}

/* site header */
.site-header{left:0;top:75px;width:1200px;height:112px;background:linear-gradient(var(--header-top),var(--header-bottom))}
.brand{left:69px;top:97px;font-family:"Roboto Slab",serif;font-weight:700;font-size:38px;line-height:46px;color:var(--white);letter-spacing:-0.5px;white-space:nowrap}
.tagline{left:69px;top:139px;font-family:"Roboto Slab",serif;font-weight:300;font-size:19px;line-height:24px;color:#d8deea;white-space:nowrap}
.search{left:366px;top:112px;width:306px;height:36px;background:#2e416b;border:1px solid #5e729c;border-radius:3px;color:#9fb0cc;font-size:16px;padding:8px 13px}
.search svg{position:absolute;right:9px;top:5px}
.topnav{left:705px;top:106px;display:flex}
.topnav-item{width:85px;height:46px;display:flex;flex-direction:column;align-items:center;justify-content:space-between;font-size:13px;line-height:15px;color:#d6dcea;border-left:1px solid #3a4a70;padding-bottom:2px}
.topnav-item:first-child{border-left:none}

/* category nav */
.catnav{left:0;top:187px;width:1200px;height:51px;background:var(--nav)}
.cat{top:201px;font-size:18.5px;line-height:24px;color:var(--white);white-space:nowrap}
.cart{left:956px;top:203px;display:flex;align-items:center;gap:10px;font-size:14px;color:var(--white);white-space:nowrap}

/* tiles */
.tile{overflow:hidden}
.photo{position:absolute;inset:0}
.tile-label{position:absolute;width:100%;text-align:center;color:var(--white)}
.kicker{font-family:"Roboto Slab",serif;font-weight:700;font-size:16px;line-height:20px}
.headline{font-family:"Roboto",sans-serif;font-weight:500;font-size:33px;line-height:38px}
.readmore{left:533px;top:553px;width:112px;height:31px;border:2px solid var(--white);font-family:"Roboto Slab",serif;font-weight:700;font-size:15px;color:var(--white);text-align:center;line-height:27px;background:rgba(0,0,0,.25);white-space:nowrap}
.promo{display:flex;align-items:center;justify-content:center}
.promo-frame{position:absolute;border:1px solid rgba(255,255,255,.45)}
.promo-text{position:relative;text-align:center;color:var(--white);font-family:"Montserrat",sans-serif}
.promo-title{font-size:20px;letter-spacing:2.5px;font-weight:500}
.promo-sub{font-size:14px;letter-spacing:1.6px;margin-top:6px;font-family:"Roboto Slab",serif}

/* product images */
.product-image{position:absolute;background:var(--product-bg)}

/* footer band */
.band{left:0;top:905px;width:1200px;height:295px;background:var(--black)}
.band-name{left:789px;top:1008px;font-family:"Roboto Slab",serif;font-weight:700;font-size:56px;line-height:70px;color:var(--white);white-space:nowrap}
</style>
</head>
<body>
<div class="canvas">

  <div class="abs tabstrip"></div>
  <div class="abs tab" style="left:0;width:212px"><span style="color:#4a78c8">✳</span>Pictures required on web p…<span class="x">×</span></div>
  <div class="abs tab" style="left:220px;width:212px"><span style="display:inline-block;width:14px;height:14px;background:#2b6cc4"></span>Mailpost - qs2741@ma…<span class="x">×</span></div>
  <div class="abs tab active" style="left:436px;width:222px">Home | Maplebarrel Winery Spe…<span class="x">×</span></div>
  <div class="abs" style="left:668px;top:6px;font-size:18px;color:#666">+</div>

  <div class="abs addressbar">
    <div class="abs url">au<span style="position:absolute;right:8px;top:3px;color:#888">▿ ↻</span></div>
    <div class="abs engine"><span class="sq"></span>Searchly</div>
  </div>

  <header class="abs site-header"></header>
  <div class="abs brand">Maplebarrel</div>
  <div class="abs tagline">Small winery specialist.</div>
  <div class="abs search">Search the Cellars
    <svg width="26" height="26" viewBox="0 0 26 26" fill="none" stroke="#e4e9f2" stroke-width="2"><circle cx="11" cy="11" r="8"/><path d="M17 17l7 7"/></svg>
  </div>
  <nav class="abs topnav">
    <div class="topnav-item"><svg width="18" height="16" viewBox="0 0 18 16" fill="#d6dcea"><path d="M9 0L0 8h3v8h4v-5h4v5h4V8h3z"/></svg>HOME</div>
    <div class="topnav-item"><svg width="22" height="16" viewBox="0 0 22 16" fill="#d6dcea"><circle cx="11" cy="4" r="3.5"/><circle cx="4" cy="5" r="2.5"/><circle cx="18" cy="5" r="2.5"/><path d="M5 16c0-5 3-7 6-7s6 2 6 7zM0 14c0-4 2-6 4-6s2 1 2 1l-2 5zM22 14c0-4-2-6-4-6s-2 1-2 1l2 5z"/></svg>ABOUT</div>
    <div class="topnav-item"><svg width="18" height="18" viewBox="0 0 18 18" fill="none" stroke="#d6dcea" stroke-width="2"><rect x="1" y="3" width="16" height="14"/><path d="M1 7h16M5 0v4M13 0v4"/></svg>EVENTS</div>
    <div class="topnav-item"><svg width="18" height="18" viewBox="0 0 18 18"><circle cx="9" cy="9" r="6" fill="none" stroke="#d6dcea" stroke-width="4" stroke-dasharray="3 2"/><circle cx="9" cy="9" r="4" fill="#d6dcea"/><circle cx="9" cy="9" r="2" fill="#25365c"/></svg>ACCOUNT</div>
    <div class="topnav-item"><svg width="16" height="16" viewBox="0 0 16 16" fill="#d6dcea"><path d="M3 0l3 4-2 2c1 2 3 4 6 6l2-2 4 3-2 3C7 16 0 9 0 3z"/></svg>CONTACT</div>
  </nav>

  <div class="abs catnav"></div>
  <nav>
    <span class="abs cat" style="left:70px">Red Wine</span>
    <span class="abs cat" style="left:180px">White Wine</span>
    <span class="abs cat" style="left:306px">Sparkling</span>
    <span class="abs cat" style="left:416px">Rosé</span>
    <span class="abs cat" style="left:490px">Old &amp; Rare</span>
    <span class="abs cat" style="left:609px">Stickies</span>
    <span class="abs cat" style="left:707px">Imported</span>
    <span class="abs cat" style="left:815px">Wine Club</span>
  </nav>
  <div class="abs cart"><svg width="24" height="22" viewBox="0 0 24 22" fill="#fff"><path d="M0 1h4l4 13h13l3-10H7l-1-3z"/><circle cx="10" cy="19" r="2"/><circle cx="19" cy="19" r="2"/></svg>Shopping cart is empty</div>

  <section class="abs tile" style="left:49px;top:253px;width:346px;height:232px">
    <div class="photo" role="img" aria-label="Wine course room with long table and chairs in front of wall shelves of bottles" style="background:linear-gradient(#4a3a2e,#2a1f18 60%,#3a2a1e)"></div>
    <div class="tile-label" style="top:78px"><div class="kicker">EDUCATION</div><div class="headline">WINE COURSES</div></div>
  </section>

  <section class="abs tile" style="left:416px;top:253px;width:348px;height:402px">
    <div class="photo" role="img" aria-label="Store owner seated beside tall wooden wine racks" style="background:linear-gradient(100deg,#5a4a3e,#3a2a22 45%,#2a1a14)"></div>
    <div class="tile-label" style="top:124px"><div class="kicker">WINE CLUB</div><div class="headline" style="margin-top:14px;font-size:32px">Let Us CHOOSE</div></div>
  </section>
  <div class="abs readmore">READ MORE</div>

  <section class="abs tile" style="left:786px;top:253px;width:346px;height:232px">
    <div class="photo" role="img" aria-label="Cellar shopfront with signage and window displays" style="background:linear-gradient(#4b5266,#2a3044 50%,#1f2436)"></div>
    <div class="tile-label" style="top:78px"><div class="kicker">PURCHASE</div><div class="headline">MIXED PACKS</div></div>
  </section>

  <section class="abs tile promo" style="left:49px;top:501px;width:346px;height:156px;background:var(--panel-red)">
    <div class="promo-frame" style="left:21px;top:22px;width:303px;height:110px"></div>
    <div class="promo-text"><div class="promo-title">FREE SHIPPING</div><div class="promo-sub">on orders over $200</div></div>
  </section>

  <section class="abs tile promo" style="left:786px;top:499px;width:346px;height:156px;background:var(--panel-navy)">
    <div class="promo-frame" style="left:20px;top:22px;width:302px;height:110px"></div>
    <div class="promo-text"><div class="promo-title">NEWSLETTER</div><div class="promo-sub" style="font-size:13.5px">join the newsletter for specials</div></div>
  </section>

  <div class="product-image" role="img" aria-label="Product photo of a red wine bottle" style="left:120px;top:692px;width:114px;height:213px"></div>
  <div class="product-image" role="img" aria-label="Product photo of a sparkling wine bottle" style="left:389px;top:690px;width:127px;height:215px"></div>
  <div class="product-image" role="img" aria-label="Product photo of a red wine bottle" style="left:680px;top:692px;width:98px;height:213px"></div>
  <div class="product-image" role="img" aria-label="Product photo of a white wine bottle" style="left:950px;top:692px;width:108px;height:213px"></div>

  <div class="abs band"></div>
  <div class="abs band-name">Maplebarrel</div>
</div>
</body>
</html>
```